UNIVERSITY OF CASTERBROOK SAXOPHONE SENIOR RECITAL

I need a poster design for my senior saxophone recital. The title of it is "Hollow: a Voyage across the Width of Tone". My concept is completely contrasting to the idea of a typical university recital. I'm so put off by the idea of "clap..clap..{play some music}..clap..clap..repeat". My recital is all based off of sound. The music I selected is all very modern (i.e Piet Halvermuss 'Warm Past the Final Pour' for Saxophone and Coffee Machine). I've included the Gatherly link so you can see the picture I have in the background. I like the idea of minimal black and white photography. Also, I would like the time / date / location / etc. all included on it. Let your imaginations run wild! It's art for an artist!
https://www.gatherly.example/events/413920587716230/
Target Market(s)
University Students around The University of Casterbrook and locals around the art district of South Beach, FL.
Industry/Entity Type
University

```html
<!DOCTYPE html>
<html lang="en">
<head>
<meta charset="utf-8">
<title>Hollow: a Voyage across the Width of Tone — Saxophone Senior Recital</title>
<link rel="stylesheet" href="https://fonts.googleapis.com/css2?family=Open+Sans:wght@400;600;700&display=swap">
<style>
  :root {
    --ink: #0b0b0b;
    --stone-dark: #1c1c1c;
    --stone-mid: #4a4a4a;
    --stone-light: #9a9a9a;
    --band-light: #a3a3a3;
    --band-mid: #7c7c7c;
    --rule: #ffffff;
    --accent: #e2591b;
    --accent-soft: #f4a273;
    --paper: #ffffff;
  }
  * { margin: 0; padding: 0; box-sizing: border-box; }
  html, body { width: 850px; height: 1200px; overflow: hidden; background: var(--ink); }
  .poster {
    position: relative;
    width: 850px;
    height: 1200px;
    overflow: hidden;
    font-family: "Open Sans", Arial, sans-serif;
  }
  .stone-photo {
    position: absolute;
    inset: 0 0 228px 0;
    background:
      radial-gradient(ellipse 300px 90px at 180px 60px, rgba(200,200,200,.45), transparent 70%),
      radial-gradient(ellipse 340px 110px at 620px 280px, rgba(190,190,190,.4), transparent 70%),
      radial-gradient(ellipse 360px 120px at 560px 500px, rgba(230,230,230,.55), transparent 70%),
      radial-gradient(ellipse 260px 90px at 120px 470px, rgba(170,170,170,.35), transparent 70%),
      radial-gradient(ellipse 320px 90px at 680px 880px, rgba(200,200,200,.45), transparent 70%),
      radial-gradient(ellipse 260px 80px at 160px 830px, rgba(170,170,170,.35), transparent 70%),
      linear-gradient(180deg, var(--stone-dark), var(--stone-mid) 30%, var(--stone-dark) 55%, var(--stone-mid) 75%, var(--stone-dark));
  }
  .stone-band {
    position: absolute;
    left: 0; right: 0; bottom: 0;
    height: 228px;
    background:
      radial-gradient(ellipse 300px 80px at 200px 170px, rgba(230,230,230,.5), transparent 70%),
      linear-gradient(180deg, var(--band-mid), var(--band-light) 60%, var(--band-mid));
  }
  .rules { position: absolute; inset: 0; z-index: 3; pointer-events: none; }
  .performer {
    position: absolute; right: 28px; top: 94px;
    font-size: 31px; font-weight: 700; letter-spacing: .5px;
    color: var(--accent-soft); line-height: 1;
  }
  .recital-type {
    position: absolute; right: 28px; top: 145px;
    font-size: 26px; font-weight: 400; color: var(--paper); line-height: 1;
  }
  .recital-type strong { font-weight: 700; }
  .title {
    position: absolute; left: 26px; top: 212px;
    font-size: 174px; font-weight: 400; letter-spacing: -4px;
    color: var(--accent); line-height: 1; z-index: 2;
  }
  .subtitle {
    position: absolute; left: 34px; top: 505px;
    font-size: 45px; font-weight: 400; letter-spacing: -.5px;
    color: var(--ink); line-height: 48px; z-index: 2;
  }
  .details {
    position: absolute; right: 28px; top: 1015px;
    text-align: right; color: var(--ink); font-weight: 700; z-index: 2;
  }
  .venue { font-size: 30px; line-height: 44px; }
  .school { font-size: 29px; line-height: 44px; }
  .when { font-size: 36px; line-height: 1; margin-top: 38px; }
</style>
</head>
<body>
  <main class="poster">
    <div class="stone-photo" role="img" aria-label="Black and white photograph of weathered stone steps with faint orange footprints climbing upward"></div>
    <div class="stone-band" role="img" aria-label="Light grey continuation of the stone steps photograph"></div>

    <svg class="rules" width="850" height="1200" viewBox="0 0 850 1200" aria-hidden="true">
      <g stroke="var(--rule)">
        <line x1="0" y1="133" x2="850" y2="133" stroke-width="2"/>
        <line x1="0" y1="345" x2="850" y2="345" stroke-width="2"/>
        <line x1="0" y1="556" x2="850" y2="556" stroke-width="1.5"/>
        <line x1="0" y1="768" x2="850" y2="768" stroke-width="2"/>
        <line x1="0" y1="972" x2="850" y2="972" stroke-width="2.5"/>
      </g>
    </svg>

    <header>
      <p class="performer">DARIO VELLACOURT</p>
      <p class="recital-type"><strong>SAXOPHONE</strong> Senior Recital</p>
    </header>

    <h1 class="title">HOLLOW:</h1>
    <h2 class="subtitle">A VOYAGE ACROSS<br>THE WIDTH OF TONE</h2>

    <footer class="details">
      <p class="venue">ASHDOWN RECITAL HALL</p>
      <p class="school">The University of Casterbrook</p>
      <p class="when">Month 01, 2013&nbsp; / &nbsp;2:00 PM</p>
    </footer>
  </main>
</body>
</html>
```